International IT business needs website revamp.

Velmont Limited would like their current website (www.velmontlimited-example.com) to be revamped/modernized to reflect up-to-date goods and services. Currently, Velmont is offering a conversational AI workflow platform for both enterprise clients and as a DIY solution for SMBs. This platform is called tqAgent and allows organizations to automate simple and repetitive workflows to drive their operational efficiency. In addition to the solution offering, Velmont Limited also provides professional IT services. With that said, please use www.velmontlimited-example.com and www.tqagent-example.ai for reference of current logos and colourways desired. Furthermore, refer to the attached PDF for a general idea of what to include in the site. The final design should be easy to navigate, clear, concise, and emphasize tqAgent as a solution for enterprise clients (while redirecting SMBs to the tqAgent website) looking to automate workflow processes/kickstart their digital transformation journey.

```html
<!DOCTYPE html>
<html lang="en">
<head>
<meta charset="utf-8">
<title>Velmont Limited – Enterprise Chatbot Platform</title>
<link href="https://fonts.googleapis.com/css2?family=Poppins:wght@400;500;600;700&family=Quicksand:wght@400;500;600;700&display=swap" rel="stylesheet">
<style>
:root{
  --blue:#1a8fd6;
  --blue-deep:#1677c0;
  --ink:#1b1b1b;
  --text:#3a3a3a;
  --muted:#666;
  --teal:#64c3b6;
  --teal-deep:#4fae9f;
  --green:#6ab04c;
  --tile:#eeeeee;
  --footer:#ececec;
  --footer-bottom:#e3e3e3;
  --dark:#333;
  --white:#fff;
}
*{margin:0;padding:0;box-sizing:border-box}
html,body{width:1200px;height:3979px;overflow:hidden}
body{position:relative;background:var(--white);font-family:"Quicksand",sans-serif;color:var(--text)}
.abs{position:absolute}
.heading{font-family:"Poppins",sans-serif}

/* header */
.brand{display:flex;align-items:center;gap:6px;font-family:"Poppins",sans-serif;font-weight:500;letter-spacing:1px;color:var(--ink)}
.brand-square{border:4px solid var(--ink);display:inline-block}
.site-header{left:117px;top:34px;width:966px;height:46px;z-index:3}
.site-header .brand{position:absolute;left:0;top:0;font-size:30px;height:46px}
.site-header .brand-square{width:46px;height:46px}
.nav{position:absolute;left:392px;top:12px;display:flex;gap:30px;font-size:15.5px;color:var(--ink);font-family:"Quicksand",sans-serif;font-weight:500}
.nav .active{color:var(--blue);text-decoration:underline}
.btn{background:var(--blue);color:var(--white);font-family:"Quicksand",sans-serif;font-weight:600;display:flex;align-items:center;justify-content:center;border-radius:2px}
.demo-btn{position:absolute;left:810px;top:3px;width:156px;height:42px;font-size:15.5px}

/* hero */
.hero-photo{left:0;top:0;width:1200px;height:661px;background:linear-gradient(90deg,#f6f6f6 0%,#f1efed 35%,#e6d6c8 60%,#cfc6bf 80%,#8b8c90 100%)}
.hero-band{left:0;top:615px;width:1200px;height:46px;background:linear-gradient(180deg,#d9d9d9,#efefef)}
.hero-title{left:127px;top:232px;font-size:62px;font-weight:700;color:var(--ink)}
.hero-sub{left:127px;top:320px;font-size:22px;line-height:31px;color:var(--ink);font-weight:500}
.dots{left:122px;top:551px;display:flex;gap:8px;align-items:center}
.dots span{width:12px;height:12px;border-radius:50%;background:#fff}
.dots .on{width:18px;height:18px;background:var(--blue)}
.product-badge{left:768px;top:443px;width:313px;height:144px;background:rgba(255,255,255,.94);display:flex;align-items:center;justify-content:center;gap:14px;font-family:"Poppins",sans-serif;font-size:40px;color:#2bb0e8}
.product-badge i{width:38px;height:38px;border-radius:50%;background:#2bb0e8;display:block}

/* clients */
.clients-intro{left:0;top:728px;width:1200px;text-align:center;font-size:14.5px;line-height:28px;color:var(--text)}
.client-tile{top:814px;width:205px;height:116px;background:var(--tile);display:flex;align-items:center;justify-content:center;font-family:"Quicksand",sans-serif;font-weight:700;font-size:30px;color:#1f5fa8}

/* about */
.about-art{left:224px;top:1058px;width:270px;height:266px;border-radius:50% 50% 46% 46%;background:radial-gradient(circle at 50% 55%,#bfe8fb 0%,#7fcff2 45%,#e9f6fd 72%,rgba(255,255,255,0) 73%)}
.about-title{left:573px;top:1040px;font-size:43px;font-weight:600;color:#2b2b2b}
.about-text{left:573px;top:1111px;width:485px;font-size:16px;line-height:30px;color:var(--text);font-weight:500}
.about-btn{left:575px;top:1325px;width:143px;height:45px;font-size:16px}

/* testimonials */
.testi-bg{left:0;top:1452px;width:1200px;height:506px}
.testi-title{left:0;top:1527px;width:1200px;text-align:center;color:#fff;font-size:34px;font-weight:600}
.testi-quote{left:0;top:1585px;width:1200px;text-align:center;color:#fff;font-size:58px;font-family:"Poppins",sans-serif;font-weight:700;line-height:1}
.testi-card{top:1690px;width:411px;height:327px;background:#fff;box-shadow:0 4px 14px rgba(0,0,0,.12);padding:52px 44px 0;text-align:center}
.testi-card p{font-size:15.5px;line-height:25.5px;color:var(--text);font-weight:500}
.testi-card h4{margin-top:20px;font-size:15.5px;font-weight:700;color:#2b2b2b}
.arrow-btn{top:2068px;width:38px;height:39px;display:flex;align-items:center;justify-content:center}

/* services */
.services-bg{left:0;top:2181px;width:1200px;height:800px;background:linear-gradient(180deg,#f7fafb,#eef5f7)}
.services-kicker{left:0;top:2262px;width:1200px;text-align:center;font-size:15.5px;color:var(--text);font-weight:500}
.services-title{left:0;top:2286px;width:1200px;text-align:center;font-size:31px;font-weight:600;color:#2b2b2b}
.services-rule{left:568px;top:2339px;width:62px;height:4px;background:var(--green)}
.hex{width:224px;height:256px}
.hex-label{width:224px;text-align:center;font-family:"Poppins",sans-serif;font-size:16.5px;line-height:25px;color:#2b2b2b;font-weight:500}
.service-card{top:2644px;width:332px;height:161px;background:#fff;box-shadow:0 3px 12px rgba(0,0,0,.08);padding:38px 0 0 50px;font-size:15.5px;line-height:24px;color:var(--text);font-weight:500}
.service-card p+p{margin-top:13px}
.center-mark{left:544px;top:2522px;width:111px;height:110px;border:9px solid #6f6f6f}

/* demo */
.demo-bg{left:0;top:2930px;width:1200px;height:620px}
.demo-title{left:233px;top:3068px;font-size:34px;color:#fff;font-weight:500}
.demo-sub{left:233px;top:3120px;font-size:23px;color:#fff;font-weight:500}
.field{background:#fff;border:1px solid #dcdcdc;font-size:14.5px;color:#444;padding:0 20px;display:flex;align-items:center;font-weight:500}
.field em{color:var(--blue);font-style:normal;margin-left:4px}
.field small{color:#999;font-size:13px;margin-left:4px}
.field-message{align-items:flex-start;padding-top:14px}
.submit-btn{left:468px;top:3351px;width:119px;height:44px;font-size:16px}

/* footer */
.footer-bg{left:0;top:3518px;width:1200px;height:400px}
.footer-brand{left:520px;top:3588px;font-size:33px;height:49px}
.footer-brand .brand-square{width:46px;height:49px}
.f-head{font-family:"Poppins",sans-serif;font-size:15px;font-weight:600;color:#2b2b2b}
.f-text{font-family:"Poppins",sans-serif;font-size:13.5px;color:#444;line-height:23px}
.quick-links{left:511px;top:3715px;font-family:"Poppins",sans-serif;font-size:13.5px;line-height:24.7px;color:#444}
.quick-links .active{color:var(--blue);text-decoration:underline}
.news-input{left:788px;top:3782px;width:295px;height:36px;background:#d7d7d7;border-radius:18px;font-size:13.5px;color:#555;padding-left:24px;display:flex;align-items:center;font-family:"Poppins",sans-serif}
.news-btn{left:964px;top:3782px;width:119px;height:36px;border-radius:18px;font-family:"Poppins",sans-serif;font-size:14px}
.footer-bottom{left:0;top:3900px;width:1200px;height:79px;background:var(--footer-bottom)}
.copyright{left:117px;top:3927px;font-family:"Poppins",sans-serif;font-size:13.5px;color:#333}
.social{left:948px;top:3920px;width:135px;height:34px;background:var(--dark);display:flex;align-items:center;justify-content:space-evenly}
.social span{width:9px;height:9px;border-radius:50%;background:#fff;display:block}
</style>
</head>
<body>

<!-- Hero -->
<div class="abs hero-photo" role="img" aria-label="Photo of a smiling support agent with a headset working at a laptop in an office chair"></div>
<div class="abs hero-band"></div>

<header class="abs site-header">
  <div class="brand"><span class="brand-square"></span>VELMONT</div>
  <nav class="nav">
    <span class="active">Home</span><span>Solutions</span><span>Services</span><span>About</span><span>Contact</span>
  </nav>
  <div class="btn demo-btn">Request a Demo</div>
</header>

<h1 class="abs heading hero-title">Could It be</h1>
<p class="abs hero-sub">Finally, an enterprise chatbot platform<br>that really delivers.</p>
<div class="abs dots"><span></span><span class="on"></span><span></span></div>
<div class="abs product-badge"><i></i>tqAgent</div>

<!-- Clients -->
<p class="abs clients-intro">Velmont's current clientele consists of businesses from many<br>sectors including Advertising, Financial and Telecommunication companies.</p>
<div class="abs client-tile" style="left:162px">Northvale</div>
<div class="abs client-tile" style="left:386px">Paylane</div>
<div class="abs client-tile" style="left:609px">Orvex</div>
<div class="abs client-tile" style="left:832px">Roadwise</div>

<!-- About -->
<div class="abs about-art" role="img" aria-label="Illustration of the friendly blue chatbot mascot wearing a headset"></div>
<h2 class="abs heading about-title">About Us</h2>
<p class="abs about-text">Since 2011, the Velmont team has been providing professional IT services for major Canadian corporations operating in the telecommunications and financial sectors. As such, our team is highly skilled in technology integration, legacy modernization, system architecture design, application development, quality assurance, project management and more!</p>
<div class="abs btn about-btn">Learn More</div>

<!-- Testimonials -->
<svg class="abs testi-bg" viewBox="0 1452 1200 506" width="1200" height="506" role="img" aria-label="Blue-tinted photo of call centre agents wearing headsets">
  <defs>
    <linearGradient id="testiGrad" x1="0" y1="0" x2="1" y2="0">
      <stop offset="0" stop-color="#1a7fc4"/>
      <stop offset="0.5" stop-color="#2a8fd2"/>
      <stop offset="1" stop-color="#3a9ad8"/>
    </linearGradient>
  </defs>
  <polygon points="0,1466 360,1460 618,1452 1200,1462 1200,1958 0,1958" fill="url(#testiGrad)"/>
</svg>
<h2 class="abs heading testi-title">Testimonials</h2>
<div class="abs testi-quote">“</div>

<article class="abs testi-card" style="left:167px">
  <p>“Leveraging tqAgent's extremely user-friendly interface, Public Service Office was able to build and implement our own bot for the My Service Account (MSA) page without the assistance of Velmont developers. By removing the need for programmers, we are able to make adjustments to our bot instantaneously!”</p>
  <h4>Civic Travel Office</h4>
</article>
<article class="abs testi-card" style="left:613px">
  <p>“Leveraging tqAgent's extremely user-friendly interface, Public Service Office was able to build and implement our own bot for the My Service Account (MSA) page without the assistance of Velmont developers. By removing the need for programmers, we are able to make adjustments to our bot instantaneously!”</p>
  <h4>Civic Travel Office</h4>
</article>

<div class="abs arrow-btn" style="left:556px;background:#4cb89a">
  <svg width="12" height="14" viewBox="0 0 12 14"><path d="M8 2 L3 7 L8 12" stroke="#fff" stroke-width="2" fill="none"/></svg>
</div>
<div class="abs arrow-btn" style="left:605px;background:#a9b4bf">
  <svg width="12" height="14" viewBox="0 0 12 14"><path d="M4 2 L9 7 L4 12" stroke="#fff" stroke-width="2" fill="none"/></svg>
</div>

<!-- Services -->
<div class="abs services-bg"></div>
<svg class="abs" style="left:0;top:2181px" width="1200" height="800" viewBox="0 0 1200 800" aria-hidden="true">
  <g stroke="#cfe3ea" stroke-width="2" fill="none">
    <path d="M690 10 L760 80 L1000 40 L1125 10 M1000 40 L1010 260 L1125 370 L1125 500 M760 80 L900 230 L1010 260 M1010 260 L1200 220"/>
    <path d="M0 120 L60 260 L0 380 M60 260 L180 300"/>
    <path d="M200 750 L375 700 L483 760 L600 700"/>
  </g>
  <g fill="#d6e9f0">
    <circle cx="1125" cy="10" r="14"/><circle cx="1010" cy="260" r="10"/><circle cx="1125" cy="370" r="10"/>
    <circle cx="900" cy="230" r="8"/><circle cx="690" cy="10" r="9"/><circle cx="375" cy="700" r="10"/>
    <circle cx="483" cy="757" r="12"/><circle cx="1125" cy="500" r="8"/>
  </g>
  <g fill="none" stroke="#4aa8d8" stroke-width="2.5">
    <circle cx="520" cy="309" r="8"/><circle cx="590" cy="284" r="7"/><circle cx="689" cy="309" r="8"/><circle cx="713" cy="247" r="7"/>
  </g>
</svg>
<p class="abs services-kicker">What services are offered?</p>
<h2 class="abs heading services-title">Our Services</h2>
<div class="abs services-rule"></div>

<svg class="abs hex" style="left:232px;top:2378px" viewBox="0 0 224 256">
  <path d="M112 4 Q118 4 124 8 L210 58 Q220 64 220 76 L220 180 Q220 192 210 198 L124 248 Q112 254 100 248 L14 198 Q4 192 4 180 L4 76 Q4 64 14 58 L100 8 Q106 4 112 4 Z" fill="#fff"/>
  <g stroke="#3f98d9" stroke-width="2" fill="none">
    <circle cx="112" cy="86" r="14"/>
    <g stroke="#6ab04c"><circle cx="112" cy="56" r="5"/><circle cx="112" cy="116" r="5"/><circle cx="82" cy="86" r="5"/><circle cx="142" cy="86" r="5"/><circle cx="90" cy="64" r="5"/><circle cx="134" cy="64" r="5"/><circle cx="90" cy="108" r="5"/><circle cx="134" cy="108" r="5"/></g>
    <path d="M112 61 V72 M112 100 V111 M87 86 H98 M126 86 H137"/>
  </g>
</svg>
<div class="abs hex-label" style="left:232px;top:2515px">DIGITAL<br>TRANSFORMATION</div>

<svg class="abs hex" style="left:736px;top:2378px" viewBox="0 0 224 256">
  <path d="M112 4 Q118 4 124 8 L210 58 Q220 64 220 76 L220 180 Q220 192 210 198 L124 248 Q112 254 100 248 L14 198 Q4 192 4 180 L4 76 Q4 64 14 58 L100 8 Q106 4 112 4 Z" fill="#fff"/>
  <g stroke-width="2.5" fill="none">
    <rect x="78" y="60" width="16" height="16" stroke="#6ab04c"/>
    <path d="M86 76 V86 H142 V96 M86 86 V96 M114 86 V96" stroke="#3f98d9"/>
    <polygon points="86,96 94,101 94,110 86,115 78,110 78,101" stroke="#3f98d9"/>
    <polygon points="114,96 122,101 122,110 114,115 106,110 106,101" stroke="#3f98d9"/>
    <circle cx="142" cy="106" r="9" stroke="#6ab04c"/>
  </g>
</svg>
<div class="abs hex-label" style="left:736px;top:2515px">NETWORK OF<br>EXPERTISE</div>

<div class="abs center-mark"></div>

<div class="abs service-card" style="left:179px">
  <p>Process Automation via RPA and<br>Conversational AI</p>
  <p>Enterprise Application Integration</p>
</div>
<div class="abs service-card" style="left:690px">
  <p>Process Automation via RPA and<br>Conversational AI</p>
  <p>Enterprise Application Integration</p>
</div>

<!-- Demo request -->
<svg class="abs demo-bg" viewBox="0 2930 1200 620" width="1200" height="620" role="img" aria-label="Teal-tinted photo of a desk with a tablet, coffee cup and plant">
  <defs>
    <linearGradient id="demoGrad" x1="0" y1="0" x2="1" y2="1">
      <stop offset="0" stop-color="#6cc8b9"/>
      <stop offset="0.6" stop-color="#5fbcae"/>
      <stop offset="1" stop-color="#52ab9e"/>
    </linearGradient>
  </defs>
  <path d="M0 2973 C250 2990 450 2955 650 2945 C850 2935 1050 2950 1200 2934 L1200 3550 L0 3550 Z" fill="url(#demoGrad)"/>
</svg>
<h2 class="abs heading demo-title">Request a Demo/PoC</h2>
<p class="abs heading demo-sub">Specialized demo/Quote</p>

<div class="abs field" style="left:229px;top:3203px;width:358px;height:46px">Full Name<em>*</em></div>
<div class="abs field" style="left:613px;top:3203px;width:358px;height:46px">Business Email Address<em>*</em></div>
<div class="abs field" style="left:229px;top:3277px;width:358px;height:47px">Phone Number<em>*</em></div>
<div class="abs field field-message" style="left:613px;top:3277px;width:358px;height:121px">Message<small>(Optional)</small></div>
<div class="abs btn submit-btn">Submit</div>

<!-- Footer -->
<svg class="abs footer-bg" viewBox="0 3518 1200 400" width="1200" height="400" aria-hidden="true">
  <polygon points="0,3540 600,3516 1200,3540 1200,3918 0,3918" fill="#ececec"/>
</svg>
<div class="abs brand footer-brand"><span class="brand-square"></span>VELMONT</div>

<h3 class="abs f-head" style="left:117px;top:3677px">Contact Us</h3>
<svg class="abs" style="left:117px;top:3716px" width="16" height="20" viewBox="0 0 16 20"><path d="M8 19 C3 12 1.5 9.5 1.5 7 A6.5 6.5 0 0 1 14.5 7 C14.5 9.5 13 12 8 19 Z" fill="none" stroke="#555" stroke-width="1.5"/><circle cx="8" cy="7" r="2.2" fill="none" stroke="#555" stroke-width="1.5"/></svg>
<p class="abs f-text" style="left:144px;top:3717px">1250 Harbour Road,<br>Unit 7 &amp; 8 Lakeview, ON<br>Canada, L0A 1B2</p>
<svg class="abs" style="left:117px;top:3797px" width="18" height="18" viewBox="0 0 18 18"><path d="M4 1 L7 5 L5 7 C6 10 8 12 11 13 L13 11 L17 14 L15 17 C8 17 1 10 1 3 Z" fill="#555"/></svg>
<p class="abs f-text" style="left:144px;top:3797px">+1 555 010 2040</p>
<svg class="abs" style="left:117px;top:3839px" width="18" height="13" viewBox="0 0 18 13"><rect x="1" y="1" width="16" height="11" fill="none" stroke="#555" stroke-width="1.3"/><path d="M1 1 L9 7 L17 1" fill="none" stroke="#555" stroke-width="1.3"/></svg>
<p class="abs f-text" style="left:144px;top:3834px">hello@velmont-example.com</p>

<h3 class="abs f-head" style="left:511px;top:3677px">Quick Links</h3>
<ul class="abs quick-links" style="list-style:none">
  <li class="active">Home</li><li>Solutions</li><li>Services</li><li>About Us</li><li>Request a Demo</li><li>Contact Us</li>
</ul>

<h3 class="abs f-head" style="left:788px;top:3677px">WRITE TO US</h3>
<p class="abs f-text" style="left:788px;top:3719px">Provide your email below to subscribe<br>to our newsletter</p>
<div class="abs news-input">Email address</div>
<div class="abs btn news-btn">Subscribe</div>

<div class="abs footer-bottom"></div>
<p class="abs copyright">Copyright 2020 Velmont</p>
<div class="abs social" aria-label="Social media links"><span></span><span></span><span></span><span></span><span></span></div>

</body>
</html>
```